VELMOTIK Amazing Business Cards Challenge

Velmoti is a new technology company that will provide engineering and manufacturing services in the electric vehicle industry.

We are looking at a new business card that will support our orientation in providing advanced, innovative solutions. The business card will be lean and present the only information required to be more efficient.

Target Market(s)

Fleet operators, private commercial vehicle operators, delivery companies.

Industry/Entity Type

Business

Contact Information for Business Card

Use the logo and its colors, use a white background.

Font styles to use
Sans Serif

Colors
0455a3
ffffff
9bcb3c

Requirements
Must have
• Velmotik Logo
• All informations in the DOC file = 3 different cards.
• White background
Nice to have
• Icons for email, phone and web address.
• Cute design and strong identity.
Should not have
• Bleeds

```html
<!DOCTYPE html>
<html lang="fr">
<head>
<meta charset="utf-8">
<title>Velmotik – cartes professionnelles</title>
<link href="https://fonts.googleapis.com/css2?family=Arimo:ital,wght@0,400;0,700;1,400;1,700&display=swap" rel="stylesheet">
<style>
  :root {
    --brand-blue: #0455a3;
    --brand-green: #9bcb3c;
    --card-white: #ffffff;
    --logo-grey: #5d5d5d;
    --stage-grey: #6e6e6e;
  }
  html, body {
    margin: 0;
    padding: 0;
    width: 1200px;
    height: 1000px;
    overflow: hidden;
    background: var(--stage-grey);
    font-family: "Arimo", Arial, sans-serif;
  }
  .sheet { position: relative; width: 1200px; height: 1000px; }
  .card {
    position: absolute;
    width: 536px;
    height: 312px;
    background: var(--card-white);
    overflow: hidden;
  }
  .card--ceo { left: 50px; top: 113px; }
  .card--bizdev { left: 610px; top: 335px; }
  .card--ops { left: 52px; top: 511px; }

  .brand {
    position: absolute;
    left: 0; right: 0; top: 14px;
    text-align: center;
  }
  .brand__mark {
    display: block;
    width: 46px; height: 46px;
    margin: 0 auto 8px;
    background: var(--brand-blue);
  }
  .brand__name {
    display: block;
    font-size: 30px;
    font-weight: 700;
    letter-spacing: 1px;
    color: var(--logo-grey);
    line-height: 1;
  }
  .person {
    position: absolute;
    left: 0; right: 0; top: 122px;
    text-align: center;
    color: var(--brand-blue);
  }
  .person__name { font-size: 19px; margin: 0; font-weight: 400; }
  .person__role { font-size: 13px; font-style: italic; margin: 6px 0 0; }

  .contact {
    position: absolute;
    left: 28px; top: 208px;
    list-style: none; margin: 0; padding: 0;
    color: var(--brand-green);
    font-size: 12px;
  }
  .contact li { display: flex; align-items: center; height: 25px; }
  .contact svg { width: 14px; height: 14px; margin-right: 10px; }

  .address {
    position: absolute;
    right: 16px; top: 238px;
    text-align: right;
    font-style: italic;
    font-size: 13px;
    line-height: 17px;
    color: var(--brand-green);
    margin: 0;
  }
  .web-band {
    position: absolute;
    left: 0; top: 281px;
    width: 253px; height: 21px;
    background: var(--brand-blue);
    color: var(--card-white);
    font-size: 14px;
    font-style: italic;
    font-weight: 700;
    line-height: 21px;
    padding-left: 50px;
    box-sizing: border-box;
    letter-spacing: 0.5px;
  }
</style>
</head>
<body>
<main class="sheet">

  <article class="card card--ceo">
    <header class="brand"><span class="brand__mark"></span><span class="brand__name">velmotik</span></header>
    <div class="person">
      <h2 class="person__name">Mathieu Bérard, ing., M.Sc.A.</h2>
      <p class="person__role">Président | CEO</p>
    </div>
    <ul class="contact">
      <li><svg viewBox="0 0 14 14"><rect x="3" y="0.5" width="8" height="13" rx="1" fill="none" stroke="currentColor" stroke-width="1.4"/><rect x="4.5" y="2.5" width="5" height="4" fill="currentColor"/></svg>+1.514.555.0142</li>
      <li><svg viewBox="0 0 14 14"><rect x="0.5" y="2.5" width="13" height="9" fill="currentColor"/><path d="M0.5 2.5 L7 8 L13.5 2.5" fill="none" stroke="#fff" stroke-width="1.2"/></svg>mberard@velmotik.com</li>
    </ul>
    <p class="address">410 – 220 Laurier Ouest, Montréal<br>(Québec) H2T 2N8 Canada</p>
    <div class="web-band">www.velmotik.com</div>
  </article>

  <article class="card card--bizdev">
    <header class="brand"><span class="brand__mark"></span><span class="brand__name">velmotik</span></header>
    <div class="person">
      <h2 class="person__name">Étienne Roy</h2>
      <p class="person__role">V.P. Développement des affaires | V.P. Business Development</p>
    </div>
    <ul class="contact">
      <li><svg viewBox="0 0 14 14"><rect x="3" y="0.5" width="8" height="13" rx="1" fill="none" stroke="currentColor" stroke-width="1.4"/><rect x="4.5" y="2.5" width="5" height="4" fill="currentColor"/></svg>+1.514.555.0163</li>
      <li><svg viewBox="0 0 14 14"><rect x="0.5" y="2.5" width="13" height="9" fill="currentColor"/><path d="M0.5 2.5 L7 8 L13.5 2.5" fill="none" stroke="#fff" stroke-width="1.2"/></svg>eroy@velmotik.com</li>
    </ul>
    <p class="address">410 – 220 Laurier Ouest, Montréal<br>(Québec) H2T 2N8 Canada</p>
    <div class="web-band">www.velmotik.com</div>
  </article>

  <article class="card card--ops">
    <header class="brand"><span class="brand__mark"></span><span class="brand__name">velmotik</span></header>
    <div class="person">
      <h2 class="person__name">Julien Marchand</h2>
      <p class="person__role">V.P. Opérations | V.P. Operations</p>
    </div>
    <ul class="contact">
      <li><svg viewBox="0 0 14 14"><rect x="3" y="0.5" width="8" height="13" rx="1" fill="none" stroke="currentColor" stroke-width="1.4"/><rect x="4.5" y="2.5" width="5" height="4" fill="currentColor"/></svg>+1.514.555-0187</li>
      <li><svg viewBox="0 0 14 14"><rect x="0.5" y="2.5" width="13" height="9" fill="currentColor"/><path d="M0.5 2.5 L7 8 L13.5 2.5" fill="none" stroke="#fff" stroke-width="1.2"/></svg>jmarchand@velmotik.com</li>
    </ul>
    <p class="address">410 – 220 Laurier Ouest, Montréal<br>(Québec) H2T 2N8 Canada</p>
    <div class="web-band">www.velmotik.com</div>
  </article>

</main>
</body>
</html>
```